Design a DL flyer double sided 4 colour 210mm x 95 mm (portrait) for the launch of a new yoga studio opening in Fernleigh Vale on the 23 November 2013.
The final design should communicate with a strong call to action- the opening date , register to receive your first class free and like us on Chatterbox.
The studio provides a tranquil, open space to practice yoga, create a feeling of light, peace and a nurturing environment, please create this feeling in the design.

An example design mock (rough design feel free to move around as required, includes final content) print specifications, logo, typography style and image attached.
The reverse side to include logo, address and please design the timetable for the launch week (refer design mock)
Have also attached a reverse logo for a dark background and are open to designer providing examples with various background colours and effects.
Back content can be moved to the front side if required to facilitate design

Target Market(s)

People in the area who are practicing yoga elsewhere and encourage them to come to the studio to try us out with a free opening offer in our first week. And people new to yoga wanting to give it a try.
Experienced yoga people and people new to yoga - all ages

Industry/Entity Type

Environment

Requirements
Must have
• The Lotus Nook logo physical address, website address, the tagline live, breathe, love...
The final design should communicate with a strong call to action- the opening date , register to receive your first class free and like us on Chatterbox. and the website address thelotusnook.com.au, drive them to the website to register.
The studio provides a tranquil, open space to practice yoga, create a feeling of light, peace and a nurturing environment, please create this feeling in the design

```html
<!DOCTYPE html>
<html lang="en">
<head>
<meta charset="utf-8">
<title>The Lotus Nook – Opening Flyer</title>
<link rel="stylesheet" href="https://fonts.googleapis.com/css2?family=Arimo:ital,wght@0,400;0,700;1,400&display=swap">
<style>
  :root {
    --ink: #222222;
    --ink-soft: #444444;
    --orange: #e8892a;
    --orange-light: #f4a640;
    --lilac: #c9c9e7;
    --label-blue: #6b8fb8;
    --rule: #cfcfcf;
    --paper: #ffffff;
    --mark: #555555;
  }
  * { margin: 0; padding: 0; box-sizing: border-box; }
  html, body { width: 1200px; height: 1000px; overflow: hidden; background: var(--paper); }
  body { position: relative; font-family: "Arimo", Arial, sans-serif; color: var(--ink); }
  .abs { position: absolute; }

  .crop-marks { position: absolute; left: 0; top: 0; }

  /* Brand lockup */
  .brand { display: flex; align-items: center; gap: 12px; }
  .brand-dot { width: 44px; height: 44px; border-radius: 50%; background: var(--orange); flex: none; }
  .brand-name { font-size: 34px; font-weight: 700; color: var(--orange); letter-spacing: -0.5px; }

  /* Front */
  .front-brand { left: 122px; top: 128px; }
  .tagline { left: 114px; top: 195px; font-size: 15px; color: var(--ink-soft); }
  .front-address { left: 114px; top: 244px; width: 298px; text-align: center; font-size: 24px; font-weight: 700; line-height: 31px; }
  .opening-line { left: 114px; top: 312px; width: 298px; text-align: center; font-size: 15.5px; }
  .offer { left: 114px; top: 343px; font-size: 18px; line-height: 22px; }
  .offer em { font-style: italic; }
  .offer-notes { left: 114px; top: 397px; width: 150px; font-size: 12.2px; line-height: 15px; }
  .offer-notes p + p { margin-top: 15px; }
  .photo-hands { left: 271px; top: 342px; width: 141px; height: 158px;
    background: radial-gradient(circle at 35% 30%, #c2344a 0%, #9a5a2a 30%, #6e6a1a 60%, #c98a54 100%); }
  .specials { left: 262px; top: 506px; width: 159px; text-align: center; font-size: 14.5px; line-height: 18.5px; }
  .photo-meditation { left: 114px; top: 566px; width: 298px; height: 247px;
    background: linear-gradient(180deg, #3f6b2a 0%, #6c9340 45%, #a9b69a 75%, #5f6f6a 100%); }
  .front-rule { left: 114px; top: 819px; width: 298px; height: 1px; background: var(--rule); }

  .info-col { top: 826px; font-size: 5.5px; line-height: 7px; color: var(--ink-soft); }
  .info-col h4 { font-size: 7px; font-weight: 400; color: var(--label-blue); letter-spacing: 0.3px; margin-bottom: 4px; }
  .info-hours { left: 120px; width: 60px; }
  .info-hours i { display: block; }
  .timetable-btn { display: block; margin-top: 6px; width: 78px; height: 9px; background: var(--orange-light);
    color: #fff; font-size: 6px; line-height: 9px; text-align: center; }
  .info-address { left: 220px; width: 90px; }
  .info-find { left: 317px; width: 85px; }
  .map-thumb { left: 314px; top: 838px; width: 86px; height: 48px; background: linear-gradient(135deg, #ece6d6, #e4dcc4); }

  /* Back */
  .back-banner { left: 776px; top: 105px; width: 299px; height: 91px; background: var(--lilac);
    display: flex; align-items: center; padding-left: 14px; }
  .back-address { left: 776px; top: 225px; font-size: 12px; letter-spacing: 0.4px; }
  .back-copy { left: 776px; top: 290px; width: 299px; font-size: 14.4px; line-height: 18px; }
  .back-copy p + p { margin-top: 18px; }
  .times-title { left: 776px; top: 584px; width: 299px; text-align: center; font-size: 12px; }
  .timetable { left: 781px; top: 614px; display: flex; font-size: 9.4px; line-height: 10.8px; }
  .timetable .day { width: 49.5px; }
  .studio-map { left: 776px; top: 694px; width: 299px; height: 203px;
    background: linear-gradient(135deg, #eee9dc 0%, #e6dfca 50%, #f1e6b8 100%); }
</style>
</head>
<body>

<svg class="crop-marks" width="1200" height="1000" viewBox="0 0 1200 1000" aria-hidden="true">
  <g stroke="var(--mark)" stroke-width="1">
    <line x1="60" y1="8" x2="60" y2="42"/><line x1="16" y1="40" x2="50" y2="40"/>
    <line x1="478" y1="8" x2="478" y2="42"/><line x1="474" y1="50" x2="508" y2="50"/>
    <line x1="710" y1="8" x2="710" y2="42"/><line x1="678" y1="50" x2="712" y2="50"/>
    <line x1="1128" y1="8" x2="1128" y2="42"/><line x1="1138" y1="40" x2="1172" y2="40"/>
    <line x1="60" y1="958" x2="60" y2="992"/><line x1="16" y1="960" x2="50" y2="960"/>
    <line x1="466" y1="958" x2="466" y2="992"/><line x1="474" y1="950" x2="508" y2="950"/>
    <line x1="710" y1="958" x2="710" y2="992"/><line x1="678" y1="950" x2="712" y2="950"/>
    <line x1="1128" y1="958" x2="1128" y2="992"/><line x1="1138" y1="960" x2="1172" y2="960"/>
  </g>
</svg>

<!-- Front side -->
<div class="abs brand front-brand"><span class="brand-dot"></span><span class="brand-name">thelotusnook</span></div>
<div class="abs tagline">Live, Breathe, Love...</div>
<h1 class="abs front-address">117 HARLOW STREET,<br>FERNLEIGH VALE</h1>
<div class="abs opening-line">New Yoga Studio opening 23 November</div>
<div class="abs offer">First class <em>Free</em><br>in opening week*</div>
<div class="abs offer-notes">
  <p>*Opening week 23 Nov -<br>29 Nov inclusive</p>
  <p>To book your free class, just go online to register and book, like us on Chatterbox The Lotus Nook - Fernleigh and tell your friends.</p>
</div>
<div class="abs photo-hands" role="img" aria-label="Close-up photo of hands resting in a meditation mudra before red tropical foliage"></div>
<div class="abs specials">View other opening specials at: thelotusnook.com.au</div>
<div class="abs photo-meditation" role="img" aria-label="Photo of a woman in white meditating cross-legged on water in a green forest"></div>
<div class="abs front-rule"></div>

<div class="abs info-col info-hours">
  <h4>OPENING HOURS</h4>
  OPEN SEVEN DAYS
  <i>See Timetable for Class Times</i>
  <span class="timetable-btn">&gt; TIMETABLE</span>
</div>
<div class="abs info-col info-address">
  <h4>ADDRESS</h4>
  117 Harlow Street<br>Fernleigh Vale FV 9021<br>hello@thelotusnook.com.au<br>Ph: 0400-555012
</div>
<div class="abs info-col info-find"><h4>FIND US</h4></div>
<div class="abs map-thumb" role="img" aria-label="Small street map with a pin marking the studio"></div>

<!-- Back side -->
<div class="abs back-banner"><div class="brand"><span class="brand-dot"></span><span class="brand-name">thelotusnook</span></div></div>
<div class="abs back-address">117 Harlow Street, Fernleigh Vale</div>
<div class="abs back-copy">
  <p>A generously sized natural studio in Fernleigh Vale, providing dynamic flow vintasa and restorative yoga for all levels from newbies to experienced, with a collection of the best teachers.</p>
  <p>Embark on a journey to happiness within yourself - be healthy in your body and mind.</p>
  <p>Science is finally proving what yogis have known all along.... yoga is good for you!</p>
  <p>A tranquil space to de-stress, build strength and healing in our bodies through our own tapas (internal heat)</p>
</div>
<div class="abs times-title">Class Times</div>
<div class="abs timetable">
  <div class="day">Mon:<br>6:30AM<br>9:30AM<br>12:30PM<br>5:30PM<br>7:00PM</div>
  <div class="day">Tue:<br>6:30AM<br>9:30AM<br>12:30PM<br>5:30PM<br>7:00PM</div>
  <div class="day">Wed:<br>6:30AM<br>9:30AM<br>12:30PM<br>5:30PM<br>7:00PM</div>
  <div class="day">Thu:<br>6:30AM<br>9:30AM<br>12:30PM<br>5:30PM<br>7:00PM</div>
  <div class="day">Fri:<br>6:30AM<br>9:30AM<br>12:30PM<br>5:30PM<br>7:00PM</div>
  <div class="day">Sat&amp;Sun:<br>9:00AM<br>10:30AM<br>4:00PM</div>
</div>
<div class="abs studio-map" role="img" aria-label="Street map of the neighbourhood with a pin marking the studio location"></div>

</body>
</html>
```